Sales Proposal Template Design

I sell Internet Marketing services; including search engine optimization, search engine marketing, social media, websites, mobile websites, email and video.

I produce a proposal for each prospective client. Some include SEO and PPC. Other include more services or less services. The purpose of this project is to create a template in PageForge or SlideLoom. I will add standard content for each product with different pricing for different projects.

I want one page for each product or service I will be presenting the the proposal. I can then use just one page or multiple pages to build the full proposal.

Once I am finished I will convert the single sheets into a PDF document to print or send to the client via email.

I am part of a the This is a KTV Franchise http://www.brevanote.example/ you can see the corporate colors and design on this website.

I would like both a vertical and horizontal orientation template.

Target Market(s)

Prospects and buyers that request information and pricing.

Industry/Entity Type

Internet

Requirements
Must have
• Must have the KTV logo and be consistent with their colors and design feel.

I need a lot of open space for content copy.

The template needs to be in PageForge or SlideLoom.
Nice to have
• A front cover design that matches the inside page template would be nice to have.

```html
<!DOCTYPE html>
<html lang="en">
<head>
<meta charset="utf-8">
<title>Internet Marketing Review and Proposal</title>
<link rel="stylesheet" href="https://fonts.googleapis.com/css2?family=Russo+One&family=Dosis:wght@400&family=Source+Sans+3:wght@400&family=Tinos:wght@400;700&display=swap">
<style>
  :root {
    --navy: #1b5d9f;
    --cyan: #2aa8e0;
    --band: #1a6bb3;
    --panel: #1fa2dc;
    --ink-dark: #1d3f6e;
    --footer-ink: #222222;
    --white: #ffffff;
    --rule: #1d3f6e;
  }
  html, body {
    margin: 0;
    padding: 0;
    overflow: hidden;
    background: var(--white);
  }
  .cover {
    position: relative;
    width: 882px;
    height: 1200px;
    overflow: hidden;
    background: var(--white);
  }
  .title {
    position: absolute;
    top: 66px;
    left: 0;
    width: 100%;
    margin: 0;
    text-align: center;
    font-family: "Russo One", sans-serif;
    font-weight: 400;
    line-height: 0.87;
  }
  .title-line {
    display: block;
    font-size: 80px;
    letter-spacing: 0;
  }
  .title-line--internet { color: var(--navy); }
  .title-line--marketing { color: var(--cyan); }
  .subtitle {
    position: absolute;
    top: 202px;
    left: 0;
    width: 100%;
    margin: 0;
    text-align: center;
    font-family: "Dosis", sans-serif;
    font-weight: 400;
    font-size: 38px;
    letter-spacing: 1px;
    color: var(--navy);
  }
  .hero-art {
    position: absolute;
    top: 252px;
    left: 140px;
    width: 640px;
    height: 360px;
  }
  .band {
    position: absolute;
    top: 636px;
    left: 0;
    width: 882px;
    height: 376px;
    background: var(--band);
  }
  .prepared-for {
    position: absolute;
    top: 636px;
    left: 40px;
    width: 282px;
    height: 326px;
    background: var(--panel);
    color: var(--white);
    text-align: center;
    font-family: "Source Sans 3", sans-serif;
  }
  .prepared-for__label {
    margin: 26px 0 14px;
    font-size: 36px;
    font-weight: 400;
    letter-spacing: 0.5px;
  }
  .prepared-for__client {
    margin: 0;
    font-size: 19px;
    line-height: 1.28;
  }
  .prepared-for__date {
    margin: 8px 0 0;
    font-size: 36px;
    line-height: 1.1;
  }
  .summary {
    position: absolute;
    top: 682px;
    left: 360px;
    width: 492px;
    color: var(--white);
    font-family: "Source Sans 3", sans-serif;
    font-size: 22px;
    line-height: 1.33;
  }
  .summary p {
    margin: 0 0 28px;
  }
  .footer {
    position: absolute;
    top: 1028px;
    left: 0;
    width: 882px;
    height: 150px;
  }
  .brand {
    position: absolute;
    top: 30px;
    left: 70px;
    display: flex;
    align-items: center;
    gap: 14px;
  }
  .brand__dot {
    width: 70px;
    height: 70px;
    border-radius: 50%;
    background: var(--navy);
  }
  .brand__name {
    font-family: "Tinos", serif;
    font-weight: 700;
    font-size: 62px;
    color: var(--navy);
    line-height: 1;
  }
  .divider {
    position: absolute;
    top: 12px;
    width: 2px;
    height: 134px;
    background: var(--rule);
  }
  .divider--first { left: 344px; }
  .divider--second { left: 564px; }
  .tagline {
    position: absolute;
    top: 48px;
    left: 368px;
    margin: 0;
    font-family: "Tinos", serif;
    font-size: 34px;
    line-height: 1.1;
    color: var(--ink-dark);
  }
  .preparer {
    position: absolute;
    top: 40px;
    left: 584px;
    margin: 0;
    font-family: "Tinos", serif;
    font-size: 18px;
    line-height: 1.4;
    color: var(--footer-ink);
    font-style: normal;
  }
</style>
</head>
<body>
  <main class="cover">
    <h1 class="title">
      <span class="title-line title-line--internet">INTERNET</span>
      <span class="title-line title-line--marketing">MARKETING</span>
    </h1>
    <p class="subtitle">REVIEW AND PROPOSAL</p>

    <svg class="hero-art" role="img" aria-label="Illustration of a blue globe at the hub of a network, linked to laptops on round blue platforms" viewBox="0 0 640 360">
      <defs>
        <radialGradient id="hero-glow" cx="50%" cy="50%" r="50%">
          <stop offset="0%" stop-color="#4f9fe0"/>
          <stop offset="60%" stop-color="#2a79c4"/>
          <stop offset="100%" stop-color="#ffffff" stop-opacity="0"/>
        </radialGradient>
      </defs>
      <rect width="640" height="360" fill="url(#hero-glow)"/>
    </svg>

    <div class="band"></div>

    <section class="prepared-for">
      <h2 class="prepared-for__label">PREPARED FOR:</h2>
      <p class="prepared-for__client">
        Dana Reyes<br>
        Practice Administrator<br>
        Harbor Bone and Motion<br>
        Port Alden,<br>
        Florida<br>
        www.harborbone.example
      </p>
      <p class="prepared-for__date">DECEMBER<br>20, 2011</p>
    </section>

    <section class="summary">
      <p>I sell Internet Marketing services; including search engine optimization, search engine marketing, social media, websites, mobile websites, email and video.</p>
      <p>I produce a proposal for each prospective client. Some include SEO and PPC. Other include more services or less services. The purpose of this project is to create a template in PageForge or SlideLoom. I will add standard content for each product with different pricing for different projects.</p>
    </section>

    <footer class="footer">
      <div class="brand">
        <span class="brand__dot"></span>
        <span class="brand__name">KTV</span>
      </div>
      <span class="divider divider--first"></span>
      <p class="tagline">clear paths<br>online</p>
      <span class="divider divider--second"></span>
      <address class="preparer">
        Prepared by: Glen Marsh<br>
        KTV Web Growth Desk<br>
        Palm Reach, Florida<br>
        www.ktvgrowth.example
      </address>
    </footer>
  </main>
</body>
</html>
```